Zerova Poultry "The Golden Crate"

I need a business card design and a logo design for my business. It's a delivery business of halal poultry (chicken). I would the business card to include the following information.
-business name: Zerova Poultry
-business tag line: "The Golden Crate"
Name: Tomas Velkor
Contact number: 07812450973
E-mail: zerova_fresh@mailvarn.com
Website: www.zerovapoultry.example
Also need a business logo also included relating to the business.
I would like it professional yet creative. Something original. I want it to have 2 main colours included.
I want it to have a middle Eastern/ Arabic look if possible.
Thanks :)
Target Market(s)
Butchers
Restaurants
Industry/Entity Type
Business
Contact Information for Business Card
Business name: Zerova poultry
Business tag line: "The Golden Crate"
E-mail: zerova_fresh@mailvarn.com
Name: Tomas Velkor
Look and feel

```html
<!DOCTYPE html>
<html lang="en">
<head>
<meta charset="UTF-8">
<title>Zerova Poultry — Business Card</title>
<link href="https://fonts.googleapis.com/css2?family=Crimson+Pro:wght@400;600;700&display=swap" rel="stylesheet">
<style>
  :root {
    --backdrop: #2f3c44;
    --card-red: #a8262a;
    --card-red-deep: #9a2226;
    --ink-white: #ffffff;
    --type-serif: "Crimson Pro", Georgia, serif;
  }
  html, body {
    margin: 0;
    padding: 0;
    width: 1200px;
    height: 900px;
    overflow: hidden;
    background: var(--backdrop);
  }
  .stage {
    width: 1200px;
    height: 900px;
    display: flex;
    align-items: center;
    justify-content: center;
  }
  .business-card {
    position: relative;
    width: 1000px;
    height: 572px;
    background: linear-gradient(160deg, var(--card-red) 0%, var(--card-red-deep) 100%);
    color: var(--ink-white);
    font-family: var(--type-serif);
  }
  .divider {
    position: absolute;
    left: 470px;
    top: 58px;
    width: 2px;
    height: 456px;
    background: var(--ink-white);
  }
  .contact-panel {
    position: absolute;
    left: 112px;
    top: 190px;
  }
  .person-name {
    margin: 0 0 30px;
    font-size: 40px;
    font-weight: 600;
    letter-spacing: 1px;
  }
  .contact-list {
    list-style: none;
    margin: 0;
    padding: 0;
  }
  .contact-item {
    display: flex;
    align-items: center;
    gap: 12px;
    font-size: 21px;
    font-weight: 600;
    margin-bottom: 14px;
  }
  .contact-icon {
    width: 22px;
    height: 22px;
    flex: none;
  }
  .brand-block {
    position: absolute;
    left: 530px;
    top: 150px;
    width: 400px;
    text-align: center;
  }
  .brand-name {
    margin: 0;
    font-size: 64px;
    font-weight: 600;
    line-height: 1.02;
  }
  .brand-mark {
    display: inline-block;
    width: 16px;
    height: 16px;
    border-radius: 50%;
    background: var(--ink-white);
    margin-bottom: 18px;
  }
  .brand-tagline {
    margin: 22px 0 0;
    font-size: 36px;
    font-weight: 400;
    letter-spacing: 1px;
    text-transform: uppercase;
  }
</style>
</head>
<body>
<main class="stage">
  <section class="business-card">
    <div class="contact-panel">
      <h1 class="person-name">Tomas Velkor</h1>
      <ul class="contact-list">
        <li class="contact-item">
          <svg class="contact-icon" viewBox="0 0 24 24" aria-hidden="true">
            <path fill="#fff" d="M6.6 10.8c1.4 2.8 3.8 5.1 6.6 6.6l2.2-2.2c.3-.3.7-.4 1-.2 1.1.4 2.3.6 3.6.6.6 0 1 .4 1 1V20c0 .6-.4 1-1 1C10.6 21 3 13.4 3 4c0-.6.4-1 1-1h3.5c.6 0 1 .4 1 1 0 1.3.2 2.5.6 3.6.1.3 0 .7-.2 1z"/>
          </svg>
          07812450973
        </li>
        <li class="contact-item">
          <svg class="contact-icon" viewBox="0 0 24 24" aria-hidden="true">
            <circle cx="12" cy="12" r="10" fill="none" stroke="#fff" stroke-width="2"/>
            <path d="M2 12h20M12 2c3 3 3 17 0 20M12 2c-3 3-3 17 0 20" fill="none" stroke="#fff" stroke-width="1.6"/>
          </svg>
          www.zerovapoultry.example
        </li>
        <li class="contact-item">
          <svg class="contact-icon" viewBox="0 0 24 24" aria-hidden="true">
            <rect x="2" y="5" width="20" height="14" fill="none" stroke="#fff" stroke-width="2"/>
            <path d="M2 5l10 8 10-8" fill="none" stroke="#fff" stroke-width="2"/>
          </svg>
          zerova_fresh@mailvarn.com
        </li>
      </ul>
    </div>

    <div class="divider"></div>

    <div class="brand-block">
      <span class="brand-mark"></span>
      <p class="brand-name">Zerova<br>Poultry</p>
      <p class="brand-tagline">The Golden Crate</p>
    </div>
  </section>
</main>
</body>
</html>
```